Prominent Law Firm Needs a New Stationary Design

We need new stationary design to go with our new logo and rustic offices.
Things we need on the letterhead:
logo (see attached file), would also like the Seven-Figure Verdict Logo (attached) somewhere on the stationary,
5182 North Pelham Avenue
Tulsa, Oklahoma 74219
(918) 555-0143 Tel ★ (918) 555-0187 Fax
www.TWVQX.example

We also need the names of the 4 partners:
Dale K. Hollingsworth
Vernon P. Hollingsworth
Mark E. Fenwicke
Tyler D. Ashcombe

And the other staff:
Brenda K. Lyle
Tendaji K. Oyelowanta
Gordon Pettijo

Hilda V. Pruitt, RN

Of Counsel:
Wendell S. Hollingsworth

Industry/Entity Type

Law Firm

```html
<!DOCTYPE html>
<html lang="en">
<head>
<meta charset="utf-8">
<title>Hollingsworth Hollingsworth Fenwicke Letterhead</title>
<link href="https://fonts.googleapis.com/css2?family=Source+Sans+3:wght@400;600;700&display=swap" rel="stylesheet">
<style>
  :root {
    --maroon: #6e1016;
    --rule: #7a1a1f;
    --sidebar-text: #ecc9c9;
    --paper: #ffffff;
    --ink: #111111;
    --watermark: #ebebeb;
  }
  * { margin: 0; padding: 0; box-sizing: border-box; }
  html, body { width: 927px; height: 1200px; overflow: hidden; background: var(--paper); }
  body { font-family: "Source Sans 3", "Myriad Pro", sans-serif; }
  .letterhead { position: relative; width: 927px; height: 1200px; background: var(--paper); }

  .sidebar { position: absolute; left: 0; top: 0; width: 212px; height: 1200px; background: var(--maroon); }
  .firm-mark {
    position: absolute; left: 15px; top: 8px; width: 185px; height: 181px; background: var(--paper);
    display: flex; flex-direction: column; align-items: center; justify-content: center; text-align: center;
    color: var(--maroon); font-weight: 700; gap: 6px;
  }
  .firm-mark .firm-name { font-size: 12px; letter-spacing: 0.5px; text-transform: uppercase; line-height: 1.2; }
  .firm-mark .firm-initials { font-size: 44px; line-height: 1; letter-spacing: 2px; }

  .roster { position: absolute; left: 0; width: 212px; text-align: center; color: var(--sidebar-text);
    font-size: 10px; line-height: 12.5px; }
  .roster.partners { top: 229px; }
  .roster.staff { top: 317px; }
  .roster.nurse { top: 391px; }
  .roster.counsel { top: 459px; }

  .verdict-badge {
    position: absolute; left: 60px; top: 1045px; width: 92px; height: 92px; border-radius: 50%;
    background: var(--paper); display: flex; align-items: center; justify-content: center; text-align: center;
    color: var(--maroon); font-weight: 700; font-size: 10px; line-height: 12px; padding: 10px;
  }

  .contact { position: absolute; right: 22px; top: 94px; text-align: right; color: var(--ink);
    font-weight: 700; font-size: 9px; line-height: 12.5px; }

  .rule { position: absolute; background: var(--rule); }
  .rule.upper { left: 318px; top: 152px; width: 587px; height: 4px; }
  .rule.lower { left: 292px; top: 163px; width: 613px; height: 3px; }

  .watermark {
    position: absolute; left: 272px; top: 400px; width: 600px; height: 360px;
    display: flex; flex-direction: column; align-items: center; justify-content: center;
    color: var(--watermark); font-weight: 700;
  }
  .watermark .watermark-initials { font-size: 190px; line-height: 1; letter-spacing: 8px; }
</style>
</head>
<body>
  <main class="letterhead">
    <aside class="sidebar">
      <div class="firm-mark">
        <span class="firm-name">Hollingsworth Hollingsworth Fenwicke</span>
        <span class="firm-initials">HHF</span>
      </div>

      <div class="roster partners">
        <p>Dale K. Hollingsworth</p>
        <p>Vernon P. Hollingsworth</p>
        <p>Mark E. Fenwicke</p>
        <p>Tyler D. Ashcombe</p>
      </div>

      <div class="roster staff">
        <p>Staff:</p>
        <p>Brenda K. Lyle</p>
        <p>Tendaji K. Oyelowanta</p>
        <p>Gordon Pettijo</p>
      </div>

      <div class="roster nurse">
        <p>Hilda V. Pruitt, RN</p>
      </div>

      <div class="roster counsel">
        <p>Of Counsel:</p>
        <p>Wendell S. Hollingsworth</p>
      </div>

      <div class="verdict-badge">Seven-Figure Verdict</div>
    </aside>

    <address class="contact">
      <p>5182 North Pelham Avenue</p>
      <p>Tulsa, Oklahoma 74219</p>
      <p>Tel (918) 555-0187 Fax (918) 555-0143</p>
      <p>www.TWVQX.example</p>
    </address>

    <div class="rule upper"></div>
    <div class="rule lower"></div>

    <div class="watermark" aria-hidden="true">
      <span class="watermark-initials">HHF</span>
    </div>
  </main>
</body>
</html>
```